Blow Dry Bar Business Cards

These cards must be eye catching and modern.
You must be willing to work fast and make changes.

Winner will be offered other projects

Files 1 THIS IS THE STYLE CARDS I AM INTRESTED IN!!!
Please be creative, I am paying for my own eye catching design. I need files to be quilla press ready.

COLORS THAT ARE PAINTED INSIDE MY SHOP:
- - - http://www.brennacoat.example/en/explore-colors/painter/color-selector.html?colors=4007-3C

- - - http://www.marlowtint.example/color/paint-colors/quiet-harbor-d58-2

I want the business cards sleek and modern if you use the logo please correct imperfections. I added the part that says Blow Dry Bar (see website).
Do not be afraid to separate the blow dryer from the name to make the cards look like the file with the pink elephant.

SHOULD INCLUDE
*Blow Dryer (we are a blow dry bar not a salon we do not cut or color so do not include sheers of any kind)
*BUSINESS NAME: Simply Swept Up - Blow Dry Bar (PLEASE SEE MY WEBSITE)
* Website: SIMPLYSWEPTUP.EXAMPLE
*Phone number (555) 314-7720
Updates

Quilla press said it can be submitted in JPG

http://www.marlowtint.example/color/paint-colors/quiet-harbor-d58-2 http://www.brennacoat.example/en/explore-colors/painter/color-selector.html?colors=4007-3C ^^^^ These links will take you to the color paint that is painted inside my shop.

Target Market(s)

AGES 18 - 55 WOMEN
HIGH END MARKET

Industry/Entity Type

Salon

Requirements
Must have
• SEE COLOR EXAMPLE FILE
BLOW DRYER
UNIQUE
I LIKE THE CARD WITH THE PINK ELEPHANT THE BEST
Nice to have
• BE AS CREATIVE AND MODERN AS POSSIBLE DO NOT COPY ANY OF THE CARDS BELOW.
Should not have
• SCISSORS
PINK

```html
<!DOCTYPE html>
<html lang="en">
<head>
<meta charset="utf-8">
<title>Simply Swept Up – Business Card</title>
<link rel="stylesheet" href="https://fonts.googleapis.com/css2?family=Poiret+One&display=swap">
<style>
  :root {
    --page: #ffffff;
    --card: #262626;
    --card-edge: #1b1b1b;
    --ink-light: #e6e6e6;
    --ink-soft: #d2d2d2;
    --badge: #efefef;
    --badge-ink: #3a3a3a;
    --rule: #bdbdbd;
    --dryer: #8a8a8a;
  }
  * { margin: 0; padding: 0; box-sizing: border-box; }
  html, body {
    width: 1057px; height: 1200px; overflow: hidden;
    background: var(--page);
    font-family: "Poiret One", sans-serif;
  }
  .card {
    position: absolute; left: 28px; width: 1005px;
    background: var(--card);
    border: 1px solid var(--card-edge);
    color: var(--ink-light);
  }
  .card--front { top: 19px; height: 574px; }
  .card--back { top: 615px; height: 577px; }

  .logo-badge {
    position: absolute; left: 364px; top: 91px;
    width: 245px; height: 245px; border-radius: 50%;
    background: var(--badge);
    display: flex; align-items: center; justify-content: center;
  }
  .logo-badge__name {
    font-size: 27px; color: var(--badge-ink); font-weight: 400;
    letter-spacing: 0.5px; white-space: nowrap;
  }
  .front-tagline {
    position: absolute; left: 0; right: 0; top: 362px;
    text-align: center; font-size: 74px; line-height: 1.1; letter-spacing: 2px;
  }

  .back-heading {
    position: absolute; left: 307px; top: 18px;
  }
  .back-heading__title { font-size: 56px; font-weight: 400; letter-spacing: 2px; line-height: 1.1; }
  .back-heading__sub { font-size: 38px; letter-spacing: 1.5px; color: var(--ink-soft); margin-left: 3px; line-height: 1.1; }

  .address {
    position: absolute; left: 34px; top: 184px;
    font-size: 39px; line-height: 44px; text-transform: uppercase;
    font-style: normal;
  }
  .divider {
    position: absolute; left: 295px; top: 127px;
    width: 1px; height: 358px; background: var(--rule);
  }
  .contact-list { list-style: none; position: absolute; left: 320px; top: 0; }
  .contact-list__item {
    position: absolute; left: 0; display: flex; align-items: center;
    white-space: nowrap; transform: translateY(-50%);
  }
  .contact-list__icon { width: 46px; height: 46px; flex: none; margin-right: 18px; }
  .contact-list__text { font-size: 38px; letter-spacing: 0.5px; }
  .contact-list__text--phone { font-size: 31px; }
  .item-phone { top: 205px; }
  .item-mail { top: 262px; }
  .item-social { top: 323px; }
  .item-updates { top: 383px; }

  .dryer-mark {
    position: absolute; left: 880px; top: 500px;
    width: 95px; height: 55px;
    background: linear-gradient(90deg, transparent, var(--dryer));
    opacity: 0.45; border-radius: 28px;
  }
</style>
</head>
<body>
  <section class="card card--front">
    <div class="logo-badge"><span class="logo-badge__name">Simply Swept Up</span></div>
    <p class="front-tagline">Premier blow dry bar</p>
  </section>

  <section class="card card--back">
    <header class="back-heading">
      <h2 class="back-heading__title">Get swept up</h2>
      <p class="back-heading__sub">contact for an appointment</p>
    </header>

    <address class="address">212 Heron<br>Bay Drive<br>Suite 8 Port<br>Linden,<br>Texas 77590</address>

    <div class="divider"></div>

    <ul class="contact-list">
      <li class="contact-list__item item-phone">
        <svg class="contact-list__icon" viewBox="0 0 46 46" aria-hidden="true">
          <circle cx="23" cy="23" r="22" fill="var(--badge)"/>
          <path d="M17 13c1.5-1 3-.5 3.5 1l1.3 3.5c.4 1-.1 2-1 2.6l-1.3.8c1 2.6 3 4.6 5.6 5.6l.8-1.3c.6-.9 1.6-1.4 2.6-1l3.5 1.3c1.5.5 2 2 1 3.5l-1.4 1.8c-1.2 1.5-3.5 1.8-5.7.7-4.8-2.4-8.6-6.2-11-11-1.1-2.2-.8-4.5.7-5.7z" fill="var(--badge-ink)"/>
        </svg>
        <span class="contact-list__text contact-list__text--phone">(555) 314-7720</span>
      </li>
      <li class="contact-list__item item-mail">
        <svg class="contact-list__icon" viewBox="0 0 46 46" aria-hidden="true">
          <circle cx="23" cy="23" r="22" fill="var(--badge)"/>
          <rect x="12" y="15" width="22" height="16" rx="2" fill="none" stroke="var(--badge-ink)" stroke-width="2.5"/>
          <path d="M13 16l10 8 10-8" fill="none" stroke="var(--badge-ink)" stroke-width="2.5"/>
        </svg>
        <span class="contact-list__text">info@simplysweptup.example</span>
      </li>
      <li class="contact-list__item item-social">
        <svg class="contact-list__icon" viewBox="0 0 46 46" aria-hidden="true">
          <circle cx="23" cy="23" r="22" fill="var(--badge)"/>
        </svg>
        <span class="contact-list__text">social.example/sweptup</span>
      </li>
      <li class="contact-list__item item-updates">
        <svg class="contact-list__icon" viewBox="0 0 46 46" aria-hidden="true">
          <circle cx="23" cy="23" r="22" fill="var(--badge)"/>
        </svg>
        <span class="contact-list__text">updates.example/sweptup</span>
      </li>
    </ul>

    <div class="dryer-mark" role="img" aria-label="Small blow dryer illustration with air streaks"></div>
  </section>
</body>
</html>
```